New Property management company business cards

Looking for a new business card, to reflect new younger ownership
Card should be clean, simple and professional but with a modern layout that is conveys our new logo and business model

Key aspects of the business:

Property Management
Facility Maintenance
Project Management
Tenant Improvements

Mailing Address:
PO BOX 7186
Larkfield CA, 95418

Phone: 555-614-8837
Direct: 555-614-8831

Doyle Farrant
President

Target Market(s)

Commercial property owners

Industry/Entity Type

Real Estate property management

Contact Information for Business Card

Open to all designs but lean toward vertical layouts

Requirements
Must have
• Logo and space to customize name and contact info

```html
<!DOCTYPE html>
<html lang="en">
<head>
<meta charset="utf-8">
<title>Vantora Property Management – Business Card</title>
<link rel="stylesheet" href="https://fonts.googleapis.com/css2?family=Montserrat:wght@400;500;700&display=swap">
<style>
  :root {
    --stage: #c9c9c9;
    --stage-dark: #a9a9a9;
    --card: #2d2c3b;
    --card-pattern: #3a3948;
    --card-deep: #262533;
    --teal: #1fa9a0;
    --white: #ffffff;
  }
  * { box-sizing: border-box; margin: 0; padding: 0; }
  html, body { width: 1200px; height: 788px; overflow: hidden; }
  body {
    background: linear-gradient(160deg, var(--stage) 0%, var(--stage-dark) 100%);
    font-family: "Montserrat", sans-serif;
    position: relative;
  }
  .card {
    position: absolute;
    width: 540px;
    height: 310px;
    background: var(--card);
    overflow: hidden;
    box-shadow: 0 14px 30px rgba(0,0,0,.28);
  }
  .card--front { left: 45px; top: 239px; }
  .card--back { left: 615px; top: 239px; }

  /* front */
  .accent-square { position: absolute; top: 0; right: 0; width: 26px; height: 26px; background: var(--teal); }
  .accent-bar { position: absolute; left: 0; bottom: 0; width: 62%; height: 7px; background: var(--teal); }
  .holder { position: absolute; top: 40px; right: 46px; text-align: right; }
  .holder__name { color: var(--teal); font-weight: 700; font-size: 22px; letter-spacing: 1.5px; text-transform: uppercase; line-height: 1.1; }
  .holder__title { color: var(--white); font-size: 13px; margin-top: 3px; }

  .brand { position: absolute; left: 40px; top: 100px; display: flex; align-items: center; gap: 10px; }
  .brand__square { width: 22px; height: 22px; background: var(--teal); flex: none; }
  .brand__name { color: var(--white); font-weight: 500; font-size: 24px; letter-spacing: 4px; line-height: 1; }
  .brand__tag { color: var(--white); font-weight: 500; font-size: 7.5px; letter-spacing: 3.2px; margin-top: 5px; }

  .contact { position: absolute; left: 40px; bottom: 32px; color: var(--white); font-size: 12px; line-height: 1.4; }
  .contact__address { margin-bottom: 9px; }
  .contact__row { display: flex; align-items: center; gap: 8px; }
  .contact__row svg { width: 10px; height: 10px; fill: var(--teal); flex: none; }

  /* back */
  .pattern { position: absolute; inset: 0; background: linear-gradient(135deg, var(--card-pattern) 0%, var(--card) 60%, var(--card-deep) 100%); }
  .back-brand { position: absolute; left: 0; right: 0; top: 92px; display: flex; justify-content: center; align-items: center; gap: 12px; }
  .back-brand__square { width: 34px; height: 34px; background: var(--teal); }
  .back-brand__name { color: var(--white); font-weight: 500; font-size: 34px; letter-spacing: 6px; line-height: 1; }
  .services { position: absolute; left: 0; right: 0; bottom: 54px; text-align: center; color: var(--white); font-size: 12.5px; line-height: 1.6; letter-spacing: .3px; }
  .services .dot { color: var(--teal); margin: 0 6px; }
</style>
</head>
<body>

<section class="card card--front" aria-label="Business card front">
  <div class="accent-square"></div>
  <div class="accent-bar"></div>

  <div class="holder">
    <p class="holder__name">Doyle Farrant</p>
    <p class="holder__title">President</p>
  </div>

  <div class="brand">
    <span class="brand__square"></span>
    <div>
      <p class="brand__name">VANTORA</p>
      <p class="brand__tag">PROPERTY MANAGEMENT</p>
    </div>
  </div>

  <div class="contact">
    <p class="contact__address">PO BOX 7186<br>Larkfield CA, 95418</p>
    <p class="contact__row">
      <svg viewBox="0 0 10 10"><rect x="2.5" y="0" width="5" height="10" rx="1"/></svg>
      555-614-8837
    </p>
    <p class="contact__row">
      <svg viewBox="0 0 10 10"><path d="M2 0 L4 2.5 L3 4 Q4.5 6 6 7 L7.5 6 L10 8 L8.5 10 Q3 9 0 1.5 Z"/></svg>
      555-614-8831
    </p>
    <p class="contact__row">
      <svg viewBox="0 0 10 10"><path d="M0 2 H10 V8 H0 Z M0 2 L5 6 L10 2"/></svg>
      info@vantoraproperty.com
    </p>
    <p class="contact__row">
      <svg viewBox="0 0 10 10"><circle cx="5" cy="5" r="5"/></svg>
      www.vantoraproperty.com
    </p>
  </div>
</section>

<section class="card card--back" aria-label="Business card back">
  <div class="pattern" role="img" aria-label="Embossed repeating brand pattern in dark slate tones"></div>

  <div class="back-brand">
    <span class="back-brand__square"></span>
    <p class="back-brand__name">VANTORA</p>
  </div>

  <p class="services">
    Property Management<span class="dot">•</span>Facility Maintenance<span class="dot">•</span>Project Management<br>
    Tenant Improvements
  </p>
</section>

</body>
</html>
```